Lend a Lantern Website Design (design layout only)

We need a website design for a new nonprofit organization based in Des Moines, Iowa called Lend a Lantern. The nonprofit provides soccer training opportunities to youth soccer players looking to improve their game while also affecting the lives of the less fortunate in a positive way. While participating in the training programs the players also go out and raise money for selected charities. The organization then donates the funds. In its first 18 months we donated $10,500. We would like to see designs attempt to symbolize the mission of the nonprofit - essentially "improve you while improving someone else."

We would like to see the following features:

· A place to donate - Our intent is to have the home page linked to the donation page; a simple straight-forward process for people to give money, and make donating as painless as possible - no account needed to make a donation, credit card or e-check should be the only information needed to donate, and have it be on a single page.

· A photo gallery so people can browse the photo gallery to get a better understanding of our organization and a place to add videos and a calendar to show upcoming events

· A place for contact information and the profiles of directors and board members. This should include a spot showing all the charities the organization donates to. Also includes a news section/blog for comments and suggestions.

We want the design to revolve around the content and mission. We would really like to stress our organization as nonprofit. We would also like if the website was user friendly and easy to navigate.

The logo of our organization is uploaded

```html
<!DOCTYPE html>
<html lang="en">
<head>
<meta charset="utf-8">
<title>Lend a Lantern</title>
<link href="https://fonts.googleapis.com/css2?family=Mulish:wght@400;600;700&display=swap" rel="stylesheet">
<style>
:root{
  --green:#85a05a;
  --green-band:#8aa15f;
  --green-dark:#4e5f30;
  --green-nav-active:#5b6f3b;
  --green-text:#7d9a4c;
  --band-ink:#2f3b1d;
  --ink:#3a3a3a;
  --body:#6b6b6b;
  --panel:#d5d5d5;
  --red:#c8272d;
  --white:#fff;
}
*{margin:0;padding:0;box-sizing:border-box}
html,body{width:821px;height:1200px;overflow:hidden}
body{position:relative;background:var(--white);font-family:"Mulish",sans-serif;color:var(--body);font-size:8.6px;line-height:1.7}
.abs{position:absolute}
.top-rule{left:0;top:0;width:821px;height:3px;background:var(--green)}
.brand{display:flex;align-items:center;gap:6px;font-weight:700;font-size:15px;color:var(--green-dark);letter-spacing:.5px;line-height:1}
.brand-mark{width:12px;height:12px;background:var(--green)}
.site-brand{left:50px;top:42px}
.search{left:605px;top:34px;width:165px;height:28px;border:1px solid #cfcfcf;border-radius:2px;font-style:italic;color:#a5a5a5;font-size:8px;padding:7px 9px;line-height:14px}
.search svg{position:absolute;right:7px;top:7px}
.nav{left:50px;top:92px;width:720px;height:29px;background:var(--green);display:flex}
.nav a{color:var(--white);text-decoration:none;font-size:9px;line-height:29px;padding:0 18px}
.nav a.active{background:var(--green-nav-active);padding:0 18px 0 17px}
.hero{left:50px;top:121px;width:720px;height:269px;background:linear-gradient(180deg,#3c5a2e 0%,#4f7a3a 30%,#3f7d2f 60%,#2d58a0 100%)}
.hero-arrow{top:239px;width:30px;height:32px;background:rgba(0,0,0,.25);display:flex;align-items:center;justify-content:center}
.section-title{font-size:16px;font-weight:400;color:var(--ink);letter-spacing:.3px;line-height:1}
.section-title span{color:var(--green-text)}
.about-title{left:50px;top:416px}
.about-text{left:50px;top:438px;width:535px}
.btn{display:inline-block;background:var(--green-dark);color:var(--white);font-size:8px;text-align:center;line-height:25px;letter-spacing:.3px}
.read-more{left:50px;top:509px;width:89px}
.divider-h{height:1px;background:#e0e0e0}
.gallery-title{left:50px;top:558px}
.gallery-text{left:50px;top:582px;width:150px}
.thumb{top:559px;width:87px;height:75px}
.donate-panel{left:605px;top:418px;width:165px;height:216px;background:var(--panel);text-align:center}
.donate-img{position:absolute;left:9px;top:8px;width:147px;height:84px;background:linear-gradient(135deg,#1c3060,#2a4680 60%,#1a2850)}
.donate-title{position:absolute;top:103px;width:100%;font-size:15px;font-weight:400;color:#1f1f1f;letter-spacing:.5px;line-height:1.2}
.donate-text{position:absolute;top:127px;left:12px;width:141px;color:#333;font-size:8px;line-height:1.8}
.donate-btn{position:absolute;left:38px;top:179px;width:89px;height:24px;line-height:24px}
.band{left:0;top:658px;width:821px;height:230px;background:var(--green-band);color:var(--white)}
.band .section-title{color:var(--white);position:absolute;top:16px}
.band-item{position:absolute;width:207px}
.band-date{font-size:8.6px;color:var(--band-ink);line-height:12px}
.band-copy{color:#f3f6ec;font-size:8.3px;line-height:14.4px}
.band-copy b{font-weight:400;color:var(--band-ink)}
.post-title{font-size:9.2px;color:var(--band-ink);line-height:12px}
.post-copy{line-height:13px}
.post-meta{font-style:italic;font-size:7.3px;color:var(--band-ink);line-height:11px}
.band-rule{position:absolute;width:207px;height:1px;background:rgba(255,255,255,.45)}
.btn-light{display:inline-block;background:#d7e2bd;color:var(--band-ink);font-size:8px;line-height:23px;padding:0 9px;position:absolute;top:191px}
.vline{position:absolute;top:16px;width:1px;height:198px;background:rgba(255,255,255,.45)}
.video{position:absolute;left:544px;top:81px;width:226px;height:128px;background:linear-gradient(180deg,#6f7f8f 0%,#8b9398 45%,#4a6a2a 75%,#3a5a22 100%);border:1px solid #5d7040}
.play{position:absolute;left:95px;top:46px}
.calendar{left:52px;top:912px;width:190px;height:152px;background:var(--white);box-shadow:0 2px 4px rgba(0,0,0,.25)}
.cal-head{height:24px;background:var(--red);color:var(--white);text-align:center;font-size:10px;line-height:24px;position:relative;letter-spacing:.5px}
.cal-head i{position:absolute;top:0;font-style:normal;font-size:7px}
.cal-ring{position:absolute;top:-10px;width:4px;height:16px;border:1.5px solid #888;border-radius:2px;background:#eee}
.cal-grid{display:grid;grid-template-columns:repeat(7,1fr);text-align:center;font-size:8px;color:#333}
.cal-grid .dow{font-size:6px;color:#888;background:#efefef;line-height:10px}
.cal-grid div.d{height:21px;line-height:17px;border-right:1px solid #eee;border-bottom:1px solid #eee;position:relative}
.cal-grid div.d.e{background:#f4f4f4}
.dot{position:absolute;left:50%;bottom:2px;width:3px;height:3px;border-radius:50%;margin-left:-1.5px}
.dot.g{background:var(--green)}
.dot.b{background:#3b7dc4}
.events-title{left:262px;top:912px}
.events{left:262px;top:936px;width:185px;color:var(--body);font-size:8.3px;line-height:1.55}
.events .band-date{color:#333;margin-top:4px;margin-bottom:2px}
.events-rule{height:1px;background:#ddd;margin:9px 0 7px}
.vline-grey{left:463px;top:912px;width:1px;height:153px;background:#e0e0e0}
.contact-title{left:485px;top:912px}
.contact{left:485px;top:938px;width:118px;color:#444;font-size:8.3px;line-height:1.6;font-style:normal;white-space:nowrap}
.contact .org{color:var(--green-dark);font-size:8.8px}
.contact b{font-weight:400;color:#111}
.contact .direction{color:var(--green-dark);margin-top:12px;font-size:8px}
.map{left:605px;top:942px;width:165px;height:137px;background:linear-gradient(135deg,#eceadf,#e3e6d6);border:1px solid #ccc}
.footer{left:0;top:1096px;width:821px;height:104px;background:linear-gradient(180deg,#e4e4e4,#f3f3f3)}
.footer-brand{left:50px;top:1120px;font-size:12px}
.copyright{left:50px;top:1170px;color:#333;font-size:7.5px}
.touch{left:550px;top:1141px;color:var(--green-dark);font-size:8px;letter-spacing:.3px}
.socials{left:658px;top:1138px;display:flex;gap:5px}
.socials span{width:19px;height:19px;border-radius:50%;background:#8e8e8e}
</style>
</head>
<body>
<div class="abs top-rule"></div>

<header>
  <div class="abs brand site-brand"><span class="brand-mark"></span>LEND A LANTERN</div>
  <div class="abs search">Search...
    <svg width="14" height="14" viewBox="0 0 14 14"><circle cx="5.5" cy="5.5" r="4" fill="none" stroke="#666" stroke-width="1.6"/><line x1="8.5" y1="8.5" x2="13" y2="13" stroke="#666" stroke-width="2"/></svg>
  </div>
  <nav class="abs nav">
    <a class="active">HOME</a><a>ABOUT US</a><a>SERVICES</a><a>GALLERY</a><a>LATEST NEWS</a><a>BLOG POSTS</a><a>DONATE</a><a>CONTACT US</a>
  </nav>
</header>

<section>
  <div class="abs hero" role="img" aria-label="Youth soccer players in blue kits sitting on a pitch listening to their coach"></div>
  <div class="abs hero-arrow" style="left:50px"><svg width="10" height="16" viewBox="0 0 10 16"><polyline points="8,1 2,8 8,15" fill="none" stroke="#fff" stroke-width="1.5"/></svg></div>
  <div class="abs hero-arrow" style="left:740px"><svg width="10" height="16" viewBox="0 0 10 16"><polyline points="2,1 8,8 2,15" fill="none" stroke="#fff" stroke-width="1.5"/></svg></div>
</section>

<section>
  <h2 class="abs section-title about-title">ABOUT OUR <span>ORGANISATION</span></h2>
  <p class="abs about-text">Aliquam molestie, mi et imperdiet euismod, dui purus auctor tellus, et interdum lacus lectus et ante. Sed accumsan sollicitudin sapien, sit amet adipiscing turpis gravida ac. In congue, neque ac lobortis volutpat, libero mauris varius mi, vitae suscipit ipsum ligula vitae risus. Duis aliquam nibh a dui iaculis viverra id a velit. Vivamus egestas risus in magna varius commodo. Sed semper viverra egestas. Etiam pretium porttitor lectus, vel ornare neque porta volutpat.</p>
  <a class="abs btn read-more">READ MORE ››</a>
  <div class="abs divider-h" style="left:50px;top:545px;width:535px"></div>
  <h2 class="abs section-title gallery-title">OUR <span>GALLERY</span></h2>
  <p class="abs gallery-text">Aliquam molestie, mi et imperdiet \euismod, dui purus auctor tellus, et interdum lacus lectus et ante...</p>
  <div class="abs thumb" style="left:213px;background:linear-gradient(180deg,#cfd8e0,#8fb06a)" role="img" aria-label="Young players contesting a header"></div>
  <div class="abs thumb" style="left:308px;background:linear-gradient(180deg,#3a5fa8,#d9c23a 60%,#5c8a3a)" role="img" aria-label="Players in yellow and blue kits on the grass"></div>
  <div class="abs thumb" style="left:404px;background:linear-gradient(180deg,#a9c4e0,#d84a4a 55%,#5d9a45)" role="img" aria-label="Player in red jumping for the ball"></div>
  <div class="abs thumb" style="left:498px;background:linear-gradient(180deg,#9fb0a0,#4a5a6a 50%,#5f9a40)" role="img" aria-label="Two players chasing the ball"></div>

  <aside class="abs donate-panel">
    <div class="donate-img" role="img" aria-label="Tipped paper cup marked help with coins spilling out"></div>
    <h3 class="donate-title">DONATE</h3>
    <p class="donate-text">Sed semper viverra egestas. Etiam pretium porttitor lectus, vel ornare neque porta volutpat.</p>
    <a class="btn donate-btn">DONATE NOW ››</a>
  </aside>
</section>

<section class="abs band">
  <h2 class="section-title" style="left:50px">LATEST NEWS</h2>
  <div class="band-item" style="left:50px;top:42px">
    <div class="band-date">JUL21, 2014</div>
    <p class="band-copy" style="margin-top:1px">Aliquam molestie, mi et imperdiet euismod, dui purus auctor tellus, et interdum lacus lectus et ante. Sed accumsan sollicitudin sapien...<b>Read More ››</b></p>
  </div>
  <div class="band-rule" style="left:50px;top:108px"></div>
  <div class="band-item" style="left:50px;top:118px">
    <div class="band-date">JUL21, 2014</div>
    <p class="band-copy" style="margin-top:1px">Aliquam molestie, mi et imperdiet euismod, dui purus auctor tellus, et interdum lacus lectus et ante. Sed accumsan sollicitudin sapien...<b>Read More ››</b></p>
  </div>
  <a class="btn-light" style="left:50px">READ ALL NEWS ››</a>
  <div class="vline" style="left:278px"></div>

  <h2 class="section-title" style="left:298px">BLOG POSTS</h2>
  <div class="band-item" style="left:298px;top:42px">
    <div class="post-title">Vestibulum ante ipsum primis in faucibus</div>
    <p class="band-copy post-copy" style="margin-top:3px">Aliquam molestie, mi et imperdiet euismod, dui purus auctor tellus, et interdum lacus lectus et ante..</p>
    <div class="post-meta" style="margin-top:3px">Reply Comments &nbsp;|&nbsp; Posted on 3days ago</div>
  </div>
  <div class="band-rule" style="left:298px;top:108px"></div>
  <div class="band-item" style="left:298px;top:118px">
    <div class="post-title">Vestibulum ante ipsum primis in faucibus</div>
    <p class="band-copy post-copy" style="margin-top:3px">Aliquam molestie, mi et imperdiet euismod, dui purus auctor tellus, et interdum lacus lectus et ante..</p>
    <div class="post-meta" style="margin-top:3px">Reply Comments &nbsp;|&nbsp; Posted on 3days ago</div>
  </div>
  <a class="btn-light" style="left:298px">READ ALL POSTS ››</a>
  <div class="vline" style="left:525px"></div>

  <h2 class="section-title" style="left:544px">VIDEOS</h2>
  <p class="band-item band-copy" style="left:544px;top:41px;width:226px">Aliquam molestie, mi et imperdiet euismod, dui purus auctor tellus, et interdum lacus lectus et ante.</p>
  <div class="video" role="img" aria-label="Video still of a soccer ball on the grass with players behind">
    <svg class="play" width="34" height="34" viewBox="0 0 34 34"><circle cx="17" cy="17" r="15" fill="rgba(0,0,0,.25)" stroke="#fff" stroke-width="2"/><polygon points="13,10 25,17 13,24" fill="#fff"/></svg>
  </div>
</section>

<section>
  <div class="abs calendar">
    <div class="cal-ring" style="left:15px"></div>
    <div class="cal-ring" style="left:171px"></div>
    <div class="cal-head"><i style="left:42px">◀</i>JULY 2014<i style="right:42px">▶</i></div>
    <div class="cal-grid">
      <div class="dow">SUN</div><div class="dow">MON</div><div class="dow">TUE</div><div class="dow">WED</div><div class="dow">THU</div><div class="dow">FRI</div><div class="dow">SAT</div>
      <div class="d">1</div><div class="d">2<span class="dot b"></span></div><div class="d">3</div><div class="d">4</div><div class="d">5<span class="dot g"></span></div><div class="d">6</div><div class="d">7</div>
      <div class="d">8</div><div class="d">9</div><div class="d">10</div><div class="d">11<span class="dot g"></span></div><div class="d">12</div><div class="d">13</div><div class="d">14</div>
      <div class="d">15</div><div class="d">16</div><div class="d">17</div><div class="d">18</div><div class="d">19<span class="dot g"></span></div><div class="d">20</div><div class="d">21</div>
      <div class="d">22<span class="dot b"></span></div><div class="d">23</div><div class="d">24</div><div class="d">25<span class="dot g" style="margin-left:-4px"></span><span class="dot b" style="margin-left:1px"></span></div><div class="d">26</div><div class="d">27</div><div class="d">28</div>
      <div class="d">29</div><div class="d">30</div><div class="d">31</div><div class="d e"></div><div class="d e"></div><div class="d e"></div><div class="d e"></div>
    </div>
  </div>

  <h2 class="abs section-title events-title">UPCOMING <span>EVENTS</span></h2>
  <div class="abs events">
    <div class="band-date">JUL21, 2014</div>
    <p>Aliquam molestie, mi et imperdiet euismod, dui purus auctor tellus, et interdum lacus lectus et ante. Sed accumsan sollicitudin sapien..</p>
    <div class="events-rule"></div>
    <div class="band-date">JUL21, 2014</div>
    <p>Aliquam molestie, mi et imperdiet euismod, dui purus auctor tellus, et interdum lacus lectus et ante. Sed accumsan sollicitudin sapien..</p>
  </div>
  <div class="abs vline-grey"></div>

  <h2 class="abs section-title contact-title">CONTACT <span>INFORMATION</span></h2>
  <address class="abs contact">
    <div class="org">LEND A LANTERN</div>
    <div>418 Lantern Way<br>Brookfield, IA 50190</div>
    <div>Ph: <b>555-014-2290</b></div>
    <div>Email: <b>hi@lendalantern.org</b></div>
    <div class="direction">GET DIRECTION ››</div>
  </address>
  <div class="abs map" role="img" aria-label="Street map of the surrounding area with a pin at the office"></div>
</section>

<footer class="abs footer"></footer>
<div class="abs brand footer-brand"><span class="brand-mark" style="width:10px;height:10px"></span>LEND A LANTERN</div>
<div class="abs copyright">Copyright © 2014. All Right Reserved</div>
<div class="abs touch">GET IN TOUCH WITH US</div>
<div class="abs socials"><span></span><span></span><span></span><span></span><span></span></div>
</body>
</html>
```